Biotech company website design

We are looking for innovative design of our upcoming website. We are a small biotechnology company in Europe dealing with life science products and services.
Updates

Please incorporate the following top level links:
ABOUT US, PRODUCTS, SERVICES, SUPPLIERS, NEWS AND PROMOS, CONTACT US

Target Market(s)

Science people, hospitals, universities ....

Industry/Entity Type

It Company

Requirements
Must have
• Must incorporate our current logo (its color toning)

```html
<!DOCTYPE html>
<html lang="en">
<head>
<meta charset="utf-8">
<title>Halvora BioSystems – About Us</title>
<link rel="stylesheet" href="https://fonts.googleapis.com/css2?family=Source+Sans+3:wght@400;600;700&display=swap">
<style>
:root{
  --green:#5fae22;
  --green-text:#56a51d;
  --ink:#4a4a4a;
  --body:#555555;
  --muted:#666666;
  --rule:#d6d6d6;
  --field:#c9c9c9;
  --white:#ffffff;
}
*{margin:0;padding:0;box-sizing:border-box}
html,body{width:1200px;height:858px;overflow:hidden;background:var(--white)}
body{font-family:"Source Sans 3",sans-serif;color:var(--body);position:relative}
a{color:inherit;text-decoration:none}
.brand{position:absolute;left:120px;top:60px;display:flex;align-items:center;gap:8px}
.brand-mark{width:32px;height:32px;background:var(--green)}
.brand-name{font-size:22px;font-weight:400;color:var(--ink);letter-spacing:-.2px}
.account-links{position:absolute;right:120px;top:83px;font-size:11.5px;color:var(--muted);display:flex;gap:8px}
.account-links .sep{color:#999}
.main-nav{position:absolute;left:120px;top:135px;display:flex;gap:40px;font-size:16px;font-weight:600;color:var(--ink)}
.main-nav .current{color:var(--green-text)}
.search{position:absolute;left:884px;top:130px;width:195px;height:29px;border:1px solid var(--field)}
.search svg{position:absolute;right:7px;top:7px}
.page-title{position:absolute;left:121px;top:184px;width:234px;height:160px;background:var(--green)}
.page-title h1{position:absolute;left:23px;top:102px;font-size:25px;font-weight:600;color:var(--white)}
.hero{position:absolute;left:359px;top:184px;width:721px;height:160px;background:linear-gradient(100deg,#3a3a3a 0%,#8a8a8a 30%,#d8d8d8 50%,#9a9a9a 70%,#3e3e3e 100%)}
.side-nav{position:absolute;left:123px;top:364px;list-style:none;font-size:14px}
.side-nav li{height:28px;line-height:28px;padding-left:15px;margin-bottom:11px;color:var(--ink)}
.side-nav .current{border-left:4px solid var(--green);padding-left:11px;color:var(--green-text);font-weight:600}
.content{position:absolute;left:363px;top:372px;width:710px}
.content h2{font-size:15px;font-weight:700;color:var(--green-text);letter-spacing:.3px;margin-left:-1px;margin-bottom:8px}
.content p{font-size:13px;line-height:24px;margin-bottom:24px;color:var(--body)}
.content .narrow{width:590px}
.site-footer{position:absolute;left:120px;top:748px;width:960px;border-top:1px solid var(--rule);padding-top:10px;font-size:11.5px;color:var(--muted);display:flex;justify-content:space-between}
.footer-nav{display:flex;gap:8px;padding-left:2px}
.footer-nav .sep{color:#999}
.copyright{padding-right:2px}
</style>
</head>
<body>
<header>
  <a class="brand" href="#"><span class="brand-mark"></span><span class="brand-name">Halvora BioSystems</span></a>
  <nav class="account-links"><a href="#">My Account</a><span class="sep">|</span><a href="#">My Cart</a><span class="sep">|</span><a href="#">My Orders</a><span class="sep">|</span><a href="#">Log in</a></nav>
  <nav class="main-nav">
    <a href="#">Home</a><a class="current" href="#">About Us</a><a href="#">Products</a><a href="#">Services</a><a href="#">Suppliers</a><a href="#">News and Promos</a><a href="#">Contact Us</a>
  </nav>
  <div class="search">
    <svg width="15" height="15" viewBox="0 0 15 15"><circle cx="6" cy="6" r="4.5" fill="none" stroke="#b5b5b5" stroke-width="2"/><line x1="9.5" y1="9.5" x2="13.5" y2="13.5" stroke="#b5b5b5" stroke-width="2.5" stroke-linecap="round"/></svg>
  </div>
</header>
<section class="page-title"><h1>About Us</h1></section>
<div class="hero" role="img" aria-label="Black and white photo looking up at glass office towers against a cloudy sky"></div>
<ul class="side-nav">
  <li class="current">About Us</li>
  <li>Vision &amp; Mision</li>
</ul>
<main class="content">
  <h2>HALVORA BIOSYSTEMS</h2>
  <p>Halvora BioSystems is an innovative company focused on developing tools for acceleration of research and applications in the field of Life Sciences. The main company expertise is in bioanalytical separations with main emphasis on DNA sequencing and DNA forensic analysis.</p>
  <p class="narrow">We supply components for improvement of durability of major components of a wide range of commercial analyzers such as DNA sequencers.</p>
  <p>Lorem ipsum dolor sit amet, consectetur adipiscing elit. Quisque felis enim, pellentesque vitae suscipit eu, fermentum in neque. Maecenas vel orci a lorem tincidunt tempus nec sed dolor. Etiam porttitor accumsan pellentesque. Quisque sapien felis, consequat at rutrum eget, euismod scelerisque mi. Praesent porta ipsum sit amet sapien tincidunt fermentum. Quisque congue quam vitae urna blandit at blandit est vulputate. Nam at nisi elit, euismod tincidunt felis. Praesent tristique convallis erat</p>
</main>
<footer class="site-footer">
  <nav class="footer-nav"><a href="#">Home</a><span class="sep">|</span><a href="#">About Us</a><span class="sep">|</span><a href="#">Products</a><span class="sep">|</span><a href="#">Services</a><span class="sep">|</span><a href="#">Suppliers</a><span class="sep">|</span><a href="#">News and Promos</a><span class="sep">|</span><a href="#">Contact Us</a></nav>
  <span class="copyright">Copyright. 2007-2013. Halvora BioSystems</span>
</footer>
</body>
</html>
```